Electronics Recycling and IT Asset Disposition Flyer and Brochure Design

We need a 2 side A5 Flyer and 4 side A4 folder( brochure) for our electronics waste recycling and IT asset management and disposition business.
Our business provides free electronics waste recycling for companies, schools, learning institutions,councils, IT companies and government sectors. Many people are ignorant of responsible recycling of electronics which could harm our health if not treated properly.
The list of other services attached in the pdf.
We provide an end to end and tailored solution for our customers from collection, logistics, data sanitisation, remarketing and recycling.

The Flyer should create awareness of responsible electronics recycling and drive the audience to contact us or go to our website to learn more about the company and services.A brief list of services should also be included in the flyer.The goal is to get the audience to contact us to enquire more about our services.

The Brochure should include all the above plus provide more details about the company, processes, services,contact details (fb, linkedin,Twitter). The goal is to convert the audience to customers for recycling and provide other services as added services.

The final design for both flyer and brochure should communicate responsible recycling of electronic scrap and tailored solution for every organisation.

The company website is www.kelvora-scrap.com.au based in Australia. We serve clients nationwide.

Target Market(s)

IT companies, Corporate, schools and learning institutions, government sector

Industry/Entity Type

Recycling

Contact Information for Business Card

Name: Darren Okefield
email: darren@kelvora-scrap.com.au
website: www.kelvora-scrap.com.au
mobile: +614 173 60294
Phone: 1300 46 2587

Font styles to use
Serif

Requirements
Must have
• I would like the designs to have more images and icons
Nice to have
Should not have
• none

```html
<!DOCTYPE html>
<html lang="en">
<head>
<meta charset="utf-8">
<title>Kelvora Scrap – Presentation Folder</title>
<link href="https://fonts.googleapis.com/css2?family=Lato:wght@400;700;900&family=Oswald:wght@700&family=Roboto+Condensed:wght@300;400&display=swap" rel="stylesheet">
<style>
  :root {
    --green-deep: #17843a;
    --green-mid: #3e9d45;
    --green-light: #7cb85b;
    --ink: #2b2b2b;
    --ink-soft: #3a3a3a;
    --paper: #ffffff;
    --paper-grey: #ececec;
    --stage: #e8e8e8;
    --stripe: #222222;
  }
  html, body {
    margin: 0;
    padding: 0;
    width: 1200px;
    height: 1200px;
    overflow: hidden;
    background: var(--stage);
  }
  .folder {
    position: absolute;
    left: 40px;
    top: 153px;
    width: 1120px;
    height: 893px;
  }
  .folder svg { display: block; width: 100%; height: 100%; }
  .contact-title {
    font-family: "Lato", sans-serif;
    font-weight: 900;
    font-size: 46px;
    fill: var(--green-deep);
  }
  .contact-line {
    font-family: "Lato", sans-serif;
    font-weight: 400;
    font-size: 28px;
    fill: var(--ink-soft);
  }
  .brand-name {
    font-family: "Lato", sans-serif;
    font-weight: 900;
    font-size: 54px;
    fill: var(--green-deep);
  }
  .headline-strong {
    font-family: "Oswald", sans-serif;
    font-weight: 700;
    font-size: 50px;
    fill: var(--green-deep);
  }
  .headline-light {
    font-family: "Roboto Condensed", sans-serif;
    font-weight: 300;
    font-size: 40px;
    fill: var(--ink);
  }
  .pocket-line {
    font-family: "Lato", sans-serif;
    font-weight: 700;
    font-size: 21px;
    fill: var(--paper);
  }
  .icon { fill: var(--green-deep); }
  .icon-light { fill: var(--paper); }
</style>
</head>
<body>
<div class="folder">
<svg viewBox="94 120 1244 992" xmlns="http://www.w3.org/2000/svg">
  <defs>
    <linearGradient id="flapGrad" x1="0" y1="0" x2="0" y2="1">
      <stop offset="0" stop-color="var(--green-deep)"/>
      <stop offset="0.5" stop-color="var(--green-light)"/>
      <stop offset="1" stop-color="var(--green-mid)"/>
    </linearGradient>
    <linearGradient id="pocketGrad" x1="0" y1="0" x2="1" y2="0">
      <stop offset="0" stop-color="var(--green-deep)"/>
      <stop offset="0.5" stop-color="var(--green-light)"/>
      <stop offset="1" stop-color="var(--green-deep)"/>
    </linearGradient>
    <linearGradient id="baseGrad" x1="0" y1="0" x2="1" y2="0">
      <stop offset="0" stop-color="var(--green-deep)"/>
      <stop offset="1" stop-color="var(--green-light)"/>
    </linearGradient>
    <linearGradient id="paperGrad" x1="0" y1="0" x2="0" y2="1">
      <stop offset="0" stop-color="#f6f6f6"/>
      <stop offset="1" stop-color="#e4e4e4"/>
    </linearGradient>
    <linearGradient id="boardGrad" x1="0" y1="0" x2="1" y2="1">
      <stop offset="0" stop-color="#b9c7bd"/>
      <stop offset="0.5" stop-color="#6f9c78"/>
      <stop offset="1" stop-color="#9fb4a4"/>
    </linearGradient>
    <linearGradient id="chipGrad" x1="0" y1="0" x2="1" y2="1">
      <stop offset="0" stop-color="#8a8f8c"/>
      <stop offset="0.5" stop-color="#d98a2c"/>
      <stop offset="1" stop-color="#6d716f"/>
    </linearGradient>
  </defs>

  <!-- side flaps -->
  <path class="flap-left" d="M94 120 H146 V825 L94 830 Z" fill="url(#flapGrad)"/>
  <path class="flap-right" d="M1286 120 H1338 V843 H1286 Z" fill="url(#flapGrad)"/>

  <!-- inside panel (left) -->
  <g class="inside-panel">
    <rect x="146" y="120" width="570" height="723" fill="url(#paperGrad)" role="img" aria-label="Faint circuit board photograph as background texture"/>
    <path class="inside-base" d="M146 825 L716 650 V843 H146 Z" fill="url(#baseGrad)"/>
    <path d="M146 818 L716 643 V652 L146 827 Z" fill="var(--stripe)"/>

    <text class="contact-title" x="415" y="296" text-anchor="middle">KELVORA</text>
    <rect x="318" y="302" width="196" height="3" fill="var(--green-deep)"/>

    <path class="icon" d="M266 334 a6 6 0 0 1 6 6 c0 5 -6 12 -6 12 c0 0 -6 -7 -6 -12 a6 6 0 0 1 6 -6 Z M266 337 a3 3 0 1 0 0.01 0 Z"/>
    <text class="contact-line" x="424" y="353" text-anchor="middle">18-22 Carrow Street,</text>
    <text class="contact-line" x="416" y="388" text-anchor="middle">Marlin Vale 2150 NSW</text>
    <path class="icon" d="M222 410 h12 v9 h-12 Z M222 410 l6 5 l6 -5" stroke="var(--paper)" stroke-width="1"/>
    <text class="contact-line" x="240" y="423">contact@kelvora-scrap.com.au</text>
    <path class="icon" d="M305 447 c2 -2 4 -1 5 1 l1 3 c0 2 -2 2 -2 3 c1 3 3 5 6 6 c1 0 1 -2 3 -2 l3 1 c2 1 3 3 1 5 c-2 2 -6 2 -10 -1 c-4 -3 -7 -7 -8 -11 c0 -2 0 -4 1 -5 Z"/>
    <text class="contact-line" x="329" y="462">1300 46 2587</text>
    <circle class="icon" cx="249" cy="489" r="7"/>
    <path d="M242 489 h14 M249 482 v14" stroke="var(--paper)" stroke-width="1.4"/>
    <text class="contact-line" x="263" y="498">www.kelvora-scrap.com.au</text>

    <!-- diamond image tiles -->
    <rect x="265" y="680" width="124" height="124" transform="rotate(45 327 742)" fill="var(--green-mid)"/>
    <rect x="275" y="688" width="124" height="124" transform="rotate(45 337 750)" fill="var(--paper)"/>
    <rect x="290" y="703" width="94" height="94" transform="rotate(45 337 750)" fill="#7cbf6a" role="img" aria-label="Recycling arrows made of green circuit board"/>
    <rect x="455" y="575" width="180" height="180" transform="rotate(45 545 665)" fill="var(--green-mid)"/>
    <rect x="465" y="585" width="180" height="180" transform="rotate(45 555 675)" fill="var(--paper)"/>
    <rect x="473" y="593" width="164" height="164" transform="rotate(45 555 675)" fill="url(#chipGrad)" role="img" aria-label="Close-up of a circuit board with an orange heatsink and recycle symbol"/>
  </g>

  <!-- cover panel (right) -->
  <g class="cover-panel">
    <rect x="716" y="120" width="570" height="723" fill="url(#paperGrad)"/>
    <text class="brand-name" x="992" y="262" text-anchor="middle">KELVORA</text>
    <text class="headline-strong" x="991" y="386" text-anchor="middle">BE RESPONSIBLE</text>
    <text class="headline-light" x="991" y="424" text-anchor="middle">TODAY FOR A BETTER</text>
    <text class="headline-light" x="991" y="462" text-anchor="middle">FUTURE TOMORROW</text>
    <path d="M716 650 L1286 478 V843 H716 Z" fill="url(#boardGrad)" role="img" aria-label="Miniature worker figures in safety vests standing on a circuit board"/>
    <path d="M700 648 L1286 457 V478 L716 660 Z" fill="var(--stripe)"/>
  </g>

  <!-- pockets -->
  <path class="pocket-left" d="M146 843 H712 L674 1090 Q670 1112 648 1112 H146 Z" fill="url(#pocketGrad)"/>
  <path class="pocket-right" d="M722 843 H1286 V1112 H784 Q762 1112 758 1090 Z" fill="url(#pocketGrad)"/>

  <g class="pocket-contact" transform="rotate(180 1004 968)">
    <circle class="icon-light" cx="894" cy="906" r="5"/>
    <text class="pocket-line" x="1010" y="913" text-anchor="middle">18-22 Carrow Street,</text>
    <text class="pocket-line" x="1010" y="941" text-anchor="middle">Marlin Vale 2150 NSW</text>
    <text class="pocket-line" x="1004" y="969" text-anchor="middle">contact@kelvora-scrap.com.au</text>
    <text class="pocket-line" x="1008" y="997" text-anchor="middle">1300 46 2587</text>
    <text class="pocket-line" x="1010" y="1025" text-anchor="middle">www.kelvora-scrap.com.au</text>
  </g>
</svg>
</div>
</body>
</html>
```